Business Card Design Project for Architecture and Interior Design company

We need a business card design and logo for an architecture and design firm located in Santiago de Chile. It´s a small company, and the name is "Ostrevo" ("Ostr" from my surname Ostrini, and "arq" for arquitectura or architecture. But it would also be nice that the logo comunicates de Word game "Bella" as beautiful in italian, and "arq" as architecture".
The idea is to give a delicate, elegant and sofisticated, yet fresh image. Would prefer grey black and white colors, but wouldn´t mind to use another additional color.
I allready have a web page www.ostrevo-studio.example, but would like to improve the logo design.
Please contact if any further information is requiered.
Reason: Need a more arquitectural and desing spirit in the cards. Few of them give that idea.

```html
<!DOCTYPE html>
<html lang="es">
<head>
<meta charset="utf-8">
<title>Ostrevo – tarjetas de presentación</title>
<link href="https://fonts.googleapis.com/css2?family=Lato:wght@300;400&display=swap" rel="stylesheet">
<style>
  :root {
    --page: #ffffff;
    --ink-black: #000000;
    --card-blue: #00628a;
    --accent: #1aa6e0;
    --accent-name: #36b6e8;
    --white: #ffffff;
    --rule: #9a9a9a;
    --icon-dot: #16263a;
    --icon-letter: #8aa0b8;
    --grey-edge: #c4c4c4;
    --grey-core: #fbfbfb;
  }
  html, body {
    margin: 0;
    padding: 0;
    width: 1200px;
    height: 1000px;
    overflow: hidden;
    background: var(--page);
    font-family: "Lato", sans-serif;
  }
  .canvas {
    position: relative;
    width: 1200px;
    height: 1000px;
    overflow: hidden;
    background: var(--page);
  }
  .card { position: absolute; overflow: hidden; }

  .card--contact {
    left: 410px; top: 20px; width: 758px; height: 428px;
    background: var(--ink-black);
  }
  .card--blue {
    left: 18px; top: 342px; width: 688px; height: 385px;
    background: var(--card-blue);
  }
  .corner-block {
    position: absolute;
    left: 0; top: 686px; width: 555px; height: 314px;
    background: var(--ink-black);
  }
  .card--grey {
    left: 555px; top: 598px; width: 645px; height: 402px;
    background: radial-gradient(ellipse at 40% 45%, var(--grey-core) 0%, #e6e6e6 45%, var(--grey-edge) 100%);
  }

  .brand {
    position: absolute;
    display: flex;
    align-items: center;
    gap: 26px;
    white-space: nowrap;
  }
  .brand__square {
    width: 60px; height: 60px;
    background: var(--accent);
    flex: none;
  }
  .brand__name {
    font-weight: 300;
    font-size: 92px;
    line-height: 1;
    letter-spacing: -1px;
  }

  .card--contact .brand { left: 42px; top: 110px; gap: 22px; }
  .card--contact .brand__square { width: 52px; height: 52px; }
  .card--contact .brand__name { color: var(--white); font-size: 78px; }

  .card--blue .brand { left: 130px; top: 127px; }
  .card--blue .brand__square { background: var(--white); }
  .card--blue .brand__name { color: var(--white); }

  .card--grey .brand { left: 96px; top: 131px; }
  .card--grey .brand__name { color: var(--ink-black); }

  .divider {
    position: absolute;
    left: 436px; top: 34px;
    width: 2px; height: 378px;
    background: var(--rule);
  }
  .person {
    position: absolute;
    left: 463px; top: 62px;
  }
  .person__name {
    margin: 0;
    font-weight: 400;
    font-size: 24px;
    color: var(--accent-name);
    letter-spacing: 0.3px;
  }
  .person__role {
    margin: 2px 0 0;
    font-weight: 400;
    font-size: 18px;
    color: var(--white);
  }
  .contact-list {
    position: absolute;
    left: 468px; top: 318px;
    margin: 0; padding: 0;
    list-style: none;
  }
  .contact-list__item {
    display: flex;
    align-items: center;
    height: 28.5px;
    color: var(--white);
    font-size: 16px;
    white-space: nowrap;
  }
  .contact-list__icon {
    width: 20px; height: 20px;
    border-radius: 50%;
    background: var(--icon-dot);
    color: var(--icon-letter);
    font-size: 12px;
    display: flex; align-items: center; justify-content: center;
    margin-right: 13px;
    flex: none;
  }
</style>
</head>
<body>
<main class="canvas">
  <section class="card card--contact">
    <div class="brand">
      <span class="brand__square"></span>
      <span class="brand__name">Ostrevo</span>
    </div>
    <div class="divider"></div>
    <div class="person">
      <p class="person__name">Marta Ostrini Vela</p>
      <p class="person__role">Arquitecto</p>
    </div>
    <ul class="contact-list">
      <li class="contact-list__item"><span class="contact-list__icon">m</span>+56 912345678</li>
      <li class="contact-list__item"><span class="contact-list__icon">e</span>mostrini@ostrevo-studio.example</li>
      <li class="contact-list__item"><span class="contact-list__icon">w</span>www.ostrevo-studio.example</li>
    </ul>
  </section>

  <section class="card card--blue">
    <div class="brand">
      <span class="brand__square"></span>
      <span class="brand__name">Ostrevo</span>
    </div>
  </section>

  <div class="corner-block"></div>

  <section class="card card--grey">
    <div class="brand">
      <span class="brand__square"></span>
      <span class="brand__name">Ostrevo</span>
    </div>
  </section>
</main>
</body>
</html>
```